Cafe & Organic Juicery in City badge (plain shape) CA

these pages need to be accessible and mobile friendly.
City badge (plain shape) mountains, the rose symbol or city design incorporated , Brick features incorporated into website since . Rustic Golds incorporated with the brick . ill attach reference pictures
Updates

Reference websites: Tidewrenpantry.example Thesaddlersniece.example Quincebarco.example

Also in the logo itself please make font on Cafe & organic match the Juicery below. It seems that it’s just a juicery due the bold writing

There is an updated version of the logo that was just added by Marlon . Please use that one with black. BAckround ( white bAckround ok at bottom of page )

Coding

Coded - Design and coding required

Number of Pages Required

5+ page

Requirements
Must have
• Mobile Friendly and functionality
• Main Page & the following pages : As tabs the brick below is from harbin stone supply and will be used for wall decoration
• Delivery Orders
• Pick up Orders / Reservations
• Menu
• Our Kombucha
• Our Coffee & Fresh pressed Juices
• About us
Nice to have
• Phone number and address should be located nicely on top of page with option to click on from mobile phones to call
• Tabs that direct to the pages referenced above should be located and easily found on the top of the main page & visible from website or mobile phone.

```html
<!DOCTYPE html>
<html lang="en">
<head>
<meta charset="utf-8">
<title>Wrenna — Cafe &amp; Organic Juicery</title>
<meta name="viewport" content="width=1200">
<link rel="stylesheet" href="https://fonts.googleapis.com/css2?family=Montserrat:wght@400;600;700&family=Open+Sans:wght@400;600&family=Cormorant+Garamond:wght@500;600&display=swap">
<style>
:root{
  --green:#4f9a5b;
  --green-dark:#3e7f49;
  --ink:#222;
  --text:#444;
  --white:#fff;
  --brick:#3b3330;
  --board:#111;
  --sand:#f2efef;
  --sky-top:#2b5d93;
  --sky-low:#7ea5cf;
}
*{box-sizing:border-box;margin:0;padding:0}
html,body{width:1200px;height:3846px;overflow:hidden}
body{position:relative;font-family:"Open Sans",Arial,sans-serif;color:var(--text);background:var(--white)}
section,header,footer{position:absolute;left:0;width:1200px}
a{text-decoration:none}
.btn{position:absolute;display:inline-block;background:var(--green);color:var(--white);font:700 14px "Montserrat",sans-serif;letter-spacing:.5px;padding:11px 26px;text-transform:uppercase;white-space:nowrap}
.btn.small{font-size:12px;padding:8px 18px}
.script{font-family:"Cormorant Garamond",Georgia,serif;font-weight:500}
.divider{position:absolute;width:60px;height:3px;background:#9a9a9a;left:570px}

/* hero */
.hero{top:0;height:692px;overflow:hidden}
.hero-photo{position:absolute;inset:0;background:linear-gradient(180deg,var(--sky-top) 0%,#3f74aa 35%,var(--sky-low) 55%,#b8a27a 72%,#3d3a33 100%)}
.brand{position:absolute;left:48px;top:30px;width:210px;height:210px;border-radius:50%;background:var(--white);border:6px solid var(--green);display:flex;align-items:center;justify-content:center;font:700 44px "Montserrat",sans-serif;color:var(--green-dark)}
.topbar{position:absolute;left:700px;top:14px;width:470px;height:44px;display:flex;justify-content:space-between;align-items:center;color:var(--white);font:600 12px "Montserrat",sans-serif;white-space:nowrap}
.topbar .item{display:flex;align-items:center;gap:10px;line-height:1.25}
.topbar .call b{display:block;font-size:20px}
.topbar small{font-size:10px}
.search{width:40px;height:40px;border:2px solid var(--white);border-radius:50%;display:flex;align-items:center;justify-content:center}
.nav{position:absolute;top:68px;left:372px;width:796px;display:flex;justify-content:space-between;font:700 11.5px "Montserrat",sans-serif;color:var(--white);text-transform:uppercase;white-space:nowrap}
.nav a{color:inherit}
.hero-title{position:absolute;right:32px;top:208px;font-size:50px;line-height:1;color:var(--white);white-space:nowrap}
.hero-sub{position:absolute;left:778px;top:280px;font:600 14px "Open Sans",sans-serif;color:var(--white);white-space:nowrap}
.dots{position:absolute;top:628px;left:545px;display:flex;gap:12px}
.dots span{width:10px;height:10px;border-radius:50%;background:var(--white)}
.dots span.on{width:14px;height:14px;margin-top:-2px;background:transparent;border:2px solid var(--white)}

/* welcome */
.welcome{top:692px;height:551px;background:#fbfbfb}
.welcome-photo{position:absolute;left:128px;top:51px;width:482px;height:444px;background:linear-gradient(180deg,#2b7fd0 0%,#8fd0f2 45%,#d5ecd2 70%,#7bb045 100%)}
.welcome .kicker{position:absolute;left:700px;top:124px;font:700 15px "Montserrat",sans-serif;color:var(--ink)}
.welcome .kicker::before{content:"";position:absolute;top:-14px;left:0;width:120px;height:2px;background:#333}
.welcome h2{position:absolute;left:700px;top:152px;font-size:38px;color:var(--ink);white-space:nowrap}
.welcome p.body{position:absolute;left:700px;top:238px;width:365px;font-size:13.5px;line-height:1.45}

/* menu */
.menu{top:1243px;height:736px;background:linear-gradient(135deg,#4a3f3b 0%,var(--brick) 50%,#2c2624 100%)}
.menu h2{position:absolute;top:40px;width:100%;text-align:center;font:700 30px "Montserrat",sans-serif;color:var(--white)}
.menu .divider{top:86px;background:var(--white)}
.board{position:absolute;background:var(--board);color:var(--white);padding:30px 34px}
.board::after{content:"";position:absolute;inset:10px;border:2px dashed #d8d8d8;pointer-events:none}
.board h3{font-size:30px;margin-bottom:16px;display:flex;justify-content:space-between;align-items:center}
.row{display:flex;justify-content:space-between;border-bottom:1px solid #333;padding:6px 0 10px;height:66px}
.row b{display:block;font:600 12.5px "Open Sans",sans-serif}
.row small{display:block;font-size:10px;line-height:1.3;color:#ccc;width:150px}
.row .price{font:600 15px "Open Sans",sans-serif}
.row .price sup{font-size:9px}

/* coffee */
.products{top:1979px;height:872px;background:var(--sand)}
.products h2{position:absolute;width:100%;text-align:center;top:62px;font:400 30px "Montserrat",sans-serif;color:var(--ink);line-height:1.35}
.products h2 b{font-weight:700}
.products .divider{top:158px}
.card{position:absolute;top:226px;width:441px}
.card .photo{height:418px}
.card h3{margin-top:28px;font:700 16px "Montserrat",sans-serif;color:var(--ink)}
.card p{margin-top:12px;font-size:13px;line-height:1.45;width:430px}
.card .btn{position:static;margin-top:18px}

/* testimonials */
.testimonials{top:2851px;height:508px;background:var(--white)}
.testimonials h2{position:absolute;width:100%;text-align:center;top:72px;font:400 30px "Montserrat",sans-serif;color:var(--ink);line-height:1.35}
.testimonials h2 b{font-weight:700}
.testimonials .divider{top:166px}
.quote-mark{position:absolute;left:314px;top:168px;font:700 64px Georgia,serif;color:var(--green);line-height:1}
.quote{position:absolute;left:350px;top:210px;width:500px;text-align:center;font-size:14px;line-height:1.45}
.arrow{position:absolute;top:252px}
.author{position:absolute;left:516px;top:362px;display:flex;align-items:center;gap:16px}
.avatar{width:56px;height:56px;border-radius:50%;background:#8a7b70}
.author b{display:block;font:700 11px "Montserrat",sans-serif;color:var(--ink)}
.author span{font-size:13px}

/* footer */
.site-footer{top:3359px;height:487px;color:var(--white)}
.footer-scene{position:absolute;inset:0;background:linear-gradient(180deg,#ffffff 0%,#dcdede 18%,#9aa2a6 38%,#5b6264 55%,#3d3f3b 75%,#2f2d28 100%)}
.footer-brand{position:absolute;left:133px;top:148px;width:200px;height:200px;border-radius:50%;border:5px solid var(--white);display:flex;align-items:center;justify-content:center;font:700 40px "Montserrat",sans-serif}
.col{position:absolute;top:196px;font-size:13px;line-height:1.4}
.col h4{font:700 12px "Montserrat",sans-serif;margin-bottom:16px}
.col li{list-style:none}
.contact li{display:flex;gap:10px;margin-bottom:16px}
.social{display:flex;gap:8px}
.social span{width:28px;height:28px;border-radius:50%;background:#1e5fa8}
.badge{position:absolute;left:943px;top:333px;width:90px;height:104px;background:var(--white)}
.badge::after{content:"";position:absolute;left:14px;top:12px;width:62px;height:62px;background:#b5212e}
.copy{position:absolute;top:412px;width:100%;text-align:center;font-size:12px}
</style>
</head>
<body>

<header class="hero">
  <div class="hero-photo" role="img" aria-label="Evening photo of a domed city hall tower with arcaded facade under a deep blue sky"></div>
  <div class="brand">Wrenna</div>
  <div class="topbar">
    <div class="item">
      <svg width="16" height="22" viewBox="0 0 18 24"><path d="M9 0C4 0 0 4 0 9c0 7 9 15 9 15s9-8 9-15c0-5-4-9-9-9zm0 12a3 3 0 110-6 3 3 0 010 6z" fill="#fff"/></svg>
      <span>118 Larkspur Lane<br>Dunmore, IL 60499</span>
    </div>
    <div class="item call">
      <svg width="26" height="26" viewBox="0 0 24 24"><path d="M6.6 10.8a15 15 0 006.6 6.6l2.2-2.2c.3-.3.7-.4 1-.2 1.1.4 2.3.6 3.6.6.6 0 1 .4 1 1V20c0 .6-.4 1-1 1A17 17 0 013 4c0-.6.4-1 1-1h3.5c.6 0 1 .4 1 1 0 1.3.2 2.5.6 3.6.1.3 0 .7-.2 1z" fill="none" stroke="#fff" stroke-width="1.6"/></svg>
      <span><small>CALL US</small><b>555.014.2200</b></span>
    </div>
    <div class="search">
      <svg width="18" height="18" viewBox="0 0 18 18"><circle cx="7.5" cy="7.5" r="5.5" fill="none" stroke="#fff" stroke-width="2"/><path d="M12 12l5 5" stroke="#fff" stroke-width="2"/></svg>
    </div>
  </div>
  <nav class="nav">
    <a href="#">Delivery Orders</a>
    <a href="#">Pick Up Orders</a>
    <a href="#">Menu</a>
    <a href="#">Our Kombucha</a>
    <a href="#">Our Coffee &amp; Fresh Pressed Juices</a>
    <a href="#">About Us</a>
  </nav>
  <h1 class="hero-title script">Cafe &amp; Organic Juicery</h1>
  <p class="hero-sub">Lorem Ipsum is simply dummy text of the printing</p>
  <a class="btn" href="#" style="left:778px;top:324px">Read More</a>
  <div class="dots"><span></span><span></span><span class="on"></span><span></span><span></span></div>
</header>

<section class="welcome">
  <div class="welcome-photo" role="img" aria-label="Two glasses of lime lemonade with ice and sliced limes beside the sea"></div>
  <p class="kicker">WELCOME TO</p>
  <h2 class="script">Cafe &amp; Organic Juicery</h2>
  <p class="body">Sed ut perspiciatis unde omnis iste natus error sit voluptatem accusantium doloremque laudantium, totam rem aperiam, eaque ipsa quae ab illo inventore veritatis et quasi architecto beatae vitae dicta sunt explicabo. Nemo enim ipsam voluptatem quia voluptas sit aspernatur aut odit aut fugi</p>
  <a class="btn" href="#" style="left:700px;top:400px">Read More</a>
</section>

<section class="menu" aria-label="Our menu">
  <h2>OUR MENU</h2>
  <div class="divider"></div>

  <div class="board" style="left:146px;top:142px;width:426px;height:487px">
    <h3 class="script">Cafe
      <svg width="40" height="34" viewBox="0 0 40 34"><path d="M4 14h26v8a10 10 0 01-10 10h-6A10 10 0 014 22z M30 16h3a4 4 0 010 8h-3" fill="none" stroke="#fff" stroke-width="2"/><path d="M12 4v6M18 2v8M24 4v6" stroke="#fff" stroke-width="2"/></svg>
    </h3>
    <div class="row"><div><b>Cool Coffee</b><small>Lorem Ipsum is simply dum my text of the printing</small></div><span class="price">$15.<sup>00</sup></span></div>
    <div class="row"><div><b>Hot Coffee</b><small>Lorem Ipsum is simply dum my text of the printing</small></div><span class="price">$15.<sup>00</sup></span></div>
    <div class="row"><div><b>Lemon Coffee</b><small>Lorem Ipsum is simply dum my text of the printing</small></div><span class="price">$15.<sup>00</sup></span></div>
    <div class="row"><div><b>Cappuccino</b><small>Lorem Ipsum is simply dum my text of the printing</small></div><span class="price">$15.<sup>00</sup></span></div>
    <div class="row"><div><b>Lattee</b><small>Lorem Ipsum is simply dum my text of the printing</small></div><span class="price">$15.<sup>00</sup></span></div>
    <div class="row" style="border:0"><div><b>Espresso</b><small>Lorem Ipsum is simply dum my text of the printing</small></div><span class="price">$15.<sup>00</sup></span></div>
  </div>

  <div class="board" style="left:613px;top:183px;width:428px;height:489px">
    <h3 class="script">Organic Juice
      <svg width="28" height="40" viewBox="0 0 28 40"><path d="M4 8h20l-3 30H7z" fill="none" stroke="#fff" stroke-width="2"/><path d="M16 8l4-7" stroke="#fff" stroke-width="2"/></svg>
    </h3>
    <div class="row"><div><b>Apple</b><small>Lorem Ipsum is simply dum my text of the printing</small></div><span class="price">$15.<sup>00</sup></span></div>
    <div class="row"><div><b>Organge</b><small>Lorem Ipsum is simply dum my text of the printing</small></div><span class="price">$15.<sup>00</sup></span></div>
    <div class="row"><div><b>Pineapple</b><small>Lorem Ipsum is simply dum my text of the printing</small></div><span class="price">$15.<sup>00</sup></span></div>
    <div class="row"><div><b>Lemon</b><small>Lorem Ipsum is simply dum my text of the printing</small></div><span class="price">$15.<sup>00</sup></span></div>
    <div class="row"><div><b>Apple</b><small>Lorem Ipsum is simply dum my text of the printing</small></div><span class="price">$15.<sup>00</sup></span></div>
    <div class="row" style="border:0"><div><b>Espresso</b><small>Lorem Ipsum is simply dum my text of the printing</small></div><span class="price">$15.<sup>00</sup></span></div>
  </div>
</section>

<section class="products">
  <h2>OUR COFFEE &amp;<br><b>FRESH PRESSED JUICES</b></h2>
  <div class="divider"></div>
  <article class="card" style="left:133px">
    <div class="photo" role="img" aria-label="Cup of latte with leaf foam art on a wooden table" style="background:radial-gradient(circle at 48% 48%,#e9d3b0 0%,#b27a45 30%,#5a3a22 60%,#3a2618 100%)"></div>
    <h3>COFFEE</h3>
    <p>Sed ut perspiciatis unde omnis iste natus error sit voluptatem accusantium sed quia consequuntur magni dolores eos qui ratione voluptatem sequi nesciunt. Neque porro quisquam.</p>
    <a class="btn small" href="#">Read More</a>
  </article>
  <article class="card" style="left:626px">
    <div class="photo" role="img" aria-label="Glass of raspberry juice with fresh raspberries and mint" style="background:radial-gradient(circle at 50% 50%,#e4415a 0%,#b01e35 35%,#4a1d22 70%,#2d1517 100%)"></div>
    <h3>FRESH JUICES</h3>
    <p>Sed ut perspiciatis unde omnis iste natus error sit voluptatem accusantium sed quia consequuntur magni dolores eos qui ratione voluptatem sequi nesciunt. Neque porro quisquam.</p>
    <a class="btn small" href="#">Read More</a>
  </article>
</section>

<section class="testimonials">
  <h2>CUSTOMER<br><b>TESTIMONIALS</b></h2>
  <div class="divider"></div>
  <div class="quote-mark">&ldquo;</div>
  <p class="quote">At vero eos et accusamus et iusto odio dignissimos ducimus qui blanditiis praesentium voluptatum deleniti atque corrupti quos dolores et quas molestias excepturi sint occaecati cupiditate non provident, similique sunt in culpa qui officia deserunt mollitia animi, id est laborum et dolorum fuga. Et harum quidem rerum facilis est et expedita distinctio. Nam libero tempore.</p>
  <svg class="arrow" style="left:186px" width="14" height="24" viewBox="0 0 14 24"><path d="M12 2L2 12l10 10" fill="none" stroke="#999" stroke-width="2"/></svg>
  <svg class="arrow" style="left:962px" width="14" height="24" viewBox="0 0 14 24"><path d="M2 2l10 10L2 22" fill="none" stroke="#999" stroke-width="2"/></svg>
  <div class="author">
    <div class="avatar" role="img" aria-label="Customer portrait"></div>
    <div><b>TOBIAS WENDELL</b><span>Canada</span></div>
  </div>
</section>

<footer class="site-footer">
  <div class="footer-scene" role="img" aria-label="Misty mountain range landscape behind the footer"></div>
  <div class="footer-brand">Wrenna</div>
  <div class="col" style="left:405px">
    <h4>MENU</h4>
    <ul>
      <li>Delivery Orders</li><li>Pick up Orders</li><li>Menu</li><li>Our Kombucha</li><li>Our Coffee &amp; Fresh pressed Juices</li><li>About us</li>
    </ul>
  </div>
  <div class="col contact" style="left:690px">
    <h4>CONTACT US</h4>
    <ul>
      <li><svg width="12" height="16" viewBox="0 0 18 24"><path d="M9 0C4 0 0 4 0 9c0 7 9 15 9 15s9-8 9-15c0-5-4-9-9-9z" fill="#fff"/></svg><span>118 Larkspur Lane<br>Dunmore, IL 60499</span></li>
      <li><svg width="14" height="14" viewBox="0 0 24 24"><path d="M6.6 10.8a15 15 0 006.6 6.6l2.2-2.2c.3-.3.7-.4 1-.2 1.1.4 2.3.6 3.6.6.6 0 1 .4 1 1V20c0 .6-.4 1-1 1A17 17 0 013 4c0-.6.4-1 1-1h3.5c.6 0 1 .4 1 1 0 1.3.2 2.5.6 3.6.1.3 0 .7-.2 1z" fill="#fff"/></svg><span>555.014.2200</span></li>
      <li><svg width="14" height="12" viewBox="0 0 14 12"><rect x="0" y="0" width="14" height="12" fill="#fff"/><path d="M0 0l7 6 7-6" fill="none" stroke="#555" stroke-width="1.2"/></svg><span>hello@wrenna.example</span></li>
    </ul>
  </div>
  <div class="col" style="left:933px">
    <h4>FOLLOW US</h4>
    <div class="social"><span></span><span></span><span></span></div>
  </div>
  <div class="badge"></div>
  <p class="copy">Copyright &copy; 2018 All Rights Reserved.</p>
</footer>

</body>
</html>
```